Advertisement Design Project for a Charity

We require an advertisement design for a local charity we are supporting

Usage: The AD will be placed in the program flyer

Charity: http://www.brightkitegala.com/

Event: Lanterns Over Maple Hollow 2013

AD Size: 7.75” w x 10” h (full page)

Our website: www.corvenfunding.ca

What we do: Corven Claim Partners Inc. provides non-recourse legal funding to plaintiffs in Canada involved in personal injury claims, before their claims settle.
Updates

hello, I posted an sample footer received from one of the designs submitted which really hit the mark with some minor corrections we would like to use.  The sample jpg of the visual has been added to the brief.

Target Market(s)

The audience will be gala participants, many of which are lawyers supporting their clients who have a child with autism.

Industry/Entity Type

Charity

Requirements
Must have
• I would like to include our company logo along with a statement about our business and a supportive message.

Examples:
Company Statement: ie. what we bring and how we help

Supportive Message:"Corven Claim Partners Inc. is proud support the Lanterns Over Maple Hollow 2013"
Should not have
• The message should not sell out services but instead support the charity and only mention what we do.

```html
<!DOCTYPE html>
<html lang="en">
<head>
<meta charset="utf-8">
<title>Corven Claim Partners Inc. supports Lanterns Over Maple Hollow 2013</title>
<link rel="stylesheet" href="https://fonts.googleapis.com/css2?family=Montserrat:wght@400;500;800&family=Great+Vibes&family=Cinzel:wght@600&display=swap">
<style>
  :root {
    --orange: #f05a28;
    --orange-deep: #e8501e;
    --amber: #f7b12a;
    --band: rgba(222, 220, 218, 0.9);
    --ink: #1b1b1b;
    --white: #ffffff;
    --sepia-dark: #2a2119;
    --sepia-light: #e6d9c6;
  }
  html, body {
    margin: 0;
    padding: 0;
    overflow: hidden;
    background: #ffffff;
  }
  .ad-page {
    position: relative;
    width: 845px;
    height: 1200px;
    overflow: hidden;
    font-family: "Montserrat", Arial, sans-serif;
  }
  .hero-photo {
    position: absolute;
    inset: 0;
    background:
      radial-gradient(ellipse 40% 30% at 45% 45%, var(--sepia-light) 0%, rgba(230,217,198,0) 70%),
      radial-gradient(ellipse 55% 40% at 70% 62%, #c9b9a3 0%, rgba(201,185,163,0) 75%),
      linear-gradient(180deg, #5a4a3b 0%, #a8937b 30%, #bfae97 55%, #6b5846 80%, var(--sepia-dark) 100%);
  }
  .sponsor-band {
    position: absolute;
    left: 0;
    top: 35px;
    width: 845px;
    height: 112px;
  }
  .sponsor-band::before {
    content: "";
    position: absolute;
    inset: 0;
    background: var(--band);
  }
  .sponsor-band__row {
    position: absolute;
    left: 150px;
    top: 64px;
    display: flex;
    align-items: baseline;
    gap: 14px;
    white-space: nowrap;
  }
  .sponsor-logo {
    display: flex;
    align-items: baseline;
    gap: 10px;
  }
  .sponsor-logo__dot {
    width: 16px;
    height: 16px;
    border-radius: 50%;
    background: var(--orange);
    align-self: center;
  }
  .sponsor-logo__name {
    font-size: 22px;
    font-weight: 500;
    color: var(--ink);
  }
  .sponsor-band__supports {
    margin: 0;
    font-size: 19px;
    font-weight: 400;
    color: var(--ink);
    letter-spacing: 0.5px;
    text-transform: uppercase;
  }
  .event-title {
    position: absolute;
    left: 0;
    top: 398px;
    width: 845px;
    margin: 0;
    font-weight: 400;
  }
  .event-title__line {
    position: absolute;
    white-space: nowrap;
    font-weight: 800;
    color: var(--orange);
    text-transform: uppercase;
    line-height: 1;
    text-shadow: 0 0 2px var(--white), 0 0 1px var(--white);
  }
  .event-title__line--first {
    left: 152px;
    top: 0;
    font-size: 70px;
  }
  .event-title__line--second {
    left: 112px;
    top: 70px;
    font-size: 66px;
  }
  .event-title__script {
    position: absolute;
    left: 330px;
    top: 100px;
    font-family: "Great Vibes", cursive;
    font-size: 118px;
    color: var(--orange);
    line-height: 1;
    -webkit-text-stroke: 1.5px var(--white);
    white-space: nowrap;
  }
  .event-title__year {
    position: absolute;
    left: 338px;
    top: 200px;
    font-size: 72px;
    font-weight: 400;
    color: var(--ink);
    line-height: 1;
  }
  .title-flourish {
    position: absolute;
    left: 312px;
    top: 645px;
    width: 222px;
    height: 85px;
    background: radial-gradient(ellipse at center, rgba(240,90,40,0.5) 0%, rgba(240,90,40,0) 70%);
  }
  .tagline {
    position: absolute;
    left: 110px;
    top: 985px;
    width: 730px;
    margin: 0;
    text-align: center;
    font-family: "Great Vibes", cursive;
    font-size: 50px;
    line-height: 1.2;
    color: var(--white);
    font-weight: 400;
    white-space: nowrap;
  }
  .company-statement {
    position: absolute;
    left: 30px;
    top: 1092px;
    width: 420px;
    margin: 0;
    font-size: 14px;
    line-height: 1.45;
    font-weight: 400;
    color: var(--white);
  }
  .web-ribbon {
    position: absolute;
    left: 470px;
    top: 1085px;
    width: 375px;
    height: 65px;
  }
  .web-ribbon svg {
    position: absolute;
    inset: 0;
  }
  .web-ribbon__url {
    position: absolute;
    right: 20px;
    top: 0;
    height: 65px;
    display: flex;
    align-items: center;
    font-family: "Cinzel", Georgia, serif;
    font-weight: 600;
    font-size: 22px;
    color: var(--white);
    letter-spacing: 0.5px;
    text-transform: uppercase;
    white-space: nowrap;
  }
</style>
</head>
<body>
<main class="ad-page">
  <div class="hero-photo" role="img" aria-label="Sepia photograph of a small child's hand holding an adult's finger, in soft focus"></div>

  <header class="sponsor-band">
    <div class="sponsor-band__row">
      <div class="sponsor-logo">
        <span class="sponsor-logo__dot"></span>
        <span class="sponsor-logo__name">Corven Claim Partners Inc.</span>
      </div>
      <p class="sponsor-band__supports">Proudly supports</p>
    </div>
  </header>

  <h1 class="event-title">
    <span class="event-title__line event-title__line--first">Lanterns</span>
    <span class="event-title__line event-title__line--second">Over Maple</span>
    <span class="event-title__script">Hollow</span>
    <span class="event-title__year">2013</span>
  </h1>

  <div class="title-flourish" role="img" aria-label="Small orange laurel ornament beneath the year"></div>

  <p class="tagline">because we care about you and your loved one...</p>

  <p class="company-statement">Corven Claim Partners Inc. provides non-recourse legal funding to personal injury plaintiffs in Canada before their claims settle.</p>

  <div class="web-ribbon">
    <svg width="375" height="65" viewBox="0 0 375 65" aria-hidden="true">
      <defs>
        <linearGradient id="ribbonFill" x1="0" y1="0" x2="1" y2="0">
          <stop offset="0" style="stop-color:#e8501e"/>
          <stop offset="1" style="stop-color:#f7b12a"/>
        </linearGradient>
      </defs>
      <polygon points="0,0 375,0 375,65 0,65 26,32.5" fill="url(#ribbonFill)"/>
    </svg>
    <span class="web-ribbon__url">www.corvenfunding.ca</span>
  </div>
</main>
</body>
</html>
```